Letterhead design of MERIDOR POWER KEEPER INC.

we are a energy saving company doing the solar screen, radian barrier, attic insulation, double panel windows. Basically i need the design of the letterhead including my company name, business address, phone numbers, fax number and email address. Main thing i need it look like a huge company and look like very high class. thanks !!

Reason: Please send me more new design about my company! Thanks so much!!

Industry/Entity Type

Business

```html
<!DOCTYPE html>
<html lang="en">
<head>
<meta charset="utf-8">
<title>Meridor Power Keeper Inc. – Letterhead</title>
<link rel="stylesheet" href="https://fonts.googleapis.com/css2?family=Cabin:wght@700&display=swap">
<style>
  :root {
    --brand-blue: #2862c6;
    --brand-deep: #1f3fa8;
    --paper: #ffffff;
  }
  html, body {
    margin: 0;
    padding: 0;
    overflow: hidden;
    background: var(--paper);
  }
  .letterhead {
    position: relative;
    width: 848px;
    height: 1200px;
    overflow: hidden;
    background: var(--paper);
    font-family: "Cabin", "Gill Sans", sans-serif;
    color: var(--brand-blue);
  }
  .brand-dot {
    position: absolute;
    left: 24px;
    top: 18px;
    width: 140px;
    height: 140px;
    border-radius: 50%;
    background: var(--brand-deep);
  }
  .corner-dot {
    position: absolute;
    left: 764px;
    top: 1114px;
    width: 70px;
    height: 70px;
    border-radius: 50%;
    background: var(--brand-deep);
  }
  .company-name {
    position: absolute;
    right: 48px;
    top: 30px;
    margin: 0;
    font-size: 42px;
    font-weight: 700;
    line-height: 1;
    letter-spacing: 0.2px;
    white-space: nowrap;
  }
  .contact {
    position: absolute;
    right: 50px;
    top: 94px;
    margin: 0;
    font-style: normal;
    text-align: right;
    font-size: 18.5px;
    font-weight: 700;
    line-height: 23.5px;
    white-space: nowrap;
  }
  .contact span { display: block; }
</style>
</head>
<body>
  <main class="letterhead">
    <div class="brand-dot" aria-hidden="true"></div>
    <h1 class="company-name">Meridor Power Keeper Inc.</h1>
    <address class="contact">
      <span class="contact-address">2280 Lanter Ave Suite #300 Houston, TEXAS 77041</span>
      <span class="contact-phone">Office phone # 555-014-2290</span>
      <span class="contact-fax">Office Fax # 555-014-2291</span>
      <span class="contact-email">Email: meridorpowerkeeper@mailbox.com</span>
    </address>
    <div class="corner-dot" aria-hidden="true"></div>
  </main>
</body>
</html>
```